New Business Card Design Project VORASTI-Italy

we are VORASTI-Italy
our company in the market for 3 years we are luxury cosmetic company and its about time for a facelift :)
i will like to have elegant luxurious and unique business card
that will give the person that get it a unique, luxurious and elegant impression
I'm VERY OPEN FOR NEW IDEAS , even duo i add a few files of things that i see on line and i like them

i add my logo as well
my website is VORASTI.COM
(if you would like to see the main style that we have)

Target Market(s)

adult that have money :)

Industry/Entity Type

Business

Contact Information for Business Card

Name - Paul Vorasti
Position - CEO and CO Founder
address - 4817 E Larkdale
telephone - 555-384-1962
email - paul@vorasti.com
fax - 555-384-1962
website - VORASTI.COM

Colors
000000
959595
fbee3e
ffffff

Requirements
Must have
• big logo in GOLD color
• elegant look
• impressive
Nice to have
• not must but maybe classy pattern background
• not must but maybe emblem
• maybe clear plastic business card
Should not have
• colors
• images

```html
<!DOCTYPE html>
<html lang="en">
<head>
<meta charset="utf-8">
<title>VORASTI Italy – Business Card</title>
<link href="https://fonts.googleapis.com/css2?family=Montserrat:wght@700;800&family=Roboto:wght@400;500&display=swap" rel="stylesheet">
<style>
  :root {
    --backdrop: #111111;
    --card-black: #000000;
    --gold: #d9b43c;
    --white: #ffffff;
    --grey: #959595;
  }
  * { margin: 0; padding: 0; box-sizing: border-box; }
  html, body {
    width: 1200px; height: 900px; overflow: hidden;
    background: var(--backdrop);
  }
  .canvas { position: relative; width: 1200px; height: 900px; }
  .card {
    position: absolute;
    width: 560px; height: 320px;
    background: var(--card-black);
    box-shadow: 0 18px 40px rgba(0,0,0,0.6);
  }
  .card-front { left: 90px; top: 120px; }
  .card-back { left: 550px; top: 460px; }

  .brand {
    position: absolute; inset: 0;
    display: flex; flex-direction: column; align-items: center; justify-content: center;
    gap: 14px;
  }
  .brand-dot {
    width: 74px; height: 74px; border-radius: 50%;
    background: var(--gold);
  }
  .brand-name {
    font-family: "Montserrat", sans-serif; font-weight: 700;
    color: var(--gold); font-size: 44px; letter-spacing: 6px;
    line-height: 1;
  }
  .brand-country {
    font-family: "Montserrat", sans-serif; font-weight: 700;
    color: var(--gold); font-size: 14px; letter-spacing: 6px;
    margin-top: -4px;
  }

  .person { position: absolute; left: 40px; top: 40px; }
  .person-name {
    font-family: "Montserrat", sans-serif; font-weight: 800;
    color: var(--gold); font-size: 26px; letter-spacing: 2px; line-height: 1;
  }
  .person-role {
    font-family: "Roboto", sans-serif; font-weight: 500;
    color: var(--white); font-size: 11px; letter-spacing: 3px;
    margin-top: 8px; margin-left: 12px;
  }
  .address {
    position: absolute; right: 36px; top: 48px; text-align: right;
    font-family: "Roboto", sans-serif; font-weight: 400;
    color: var(--white); font-size: 11px; letter-spacing: 2px; line-height: 1.6;
  }
  .contact {
    position: absolute; left: 110px; bottom: 34px;
    font-family: "Roboto", sans-serif; font-weight: 400;
    color: var(--white); font-size: 11px; letter-spacing: 2px; line-height: 1.6;
  }
</style>
</head>
<body>
<main class="canvas">
  <section class="card card-front" aria-label="Card front">
    <div class="brand">
      <span class="brand-dot"></span>
      <span class="brand-name">VORASTI</span>
      <span class="brand-country">ITALY</span>
    </div>
  </section>

  <section class="card card-back" aria-label="Card back">
    <div class="person">
      <p class="person-name">MARCO DELRIN</p>
      <p class="person-role">MANAGER</p>
    </div>
    <address class="address">
      LARKDALE COMPLEX<br>
      VERANO, SOLMARA<br>
      40218
    </address>
    <div class="contact">
      <p>123 1234 12</p>
      <p>123 1234 12</p>
      <p>MARCO@MAIL.COM</p>
      <p>WWW.MARCODELRIN.COM</p>
    </div>
  </section>
</main>
</body>
</html>
```